Shaker Barons business card

We would like a business card designed for our business shaker barons

We need it to have 2 sides.

More information about the business can be found at www.shakerbarons.net

```html
<!DOCTYPE html>
<html lang="en">
<head>
<meta charset="utf-8">
<title>Shaker Barons business card</title>
<link href="https://fonts.googleapis.com/css2?family=Lobster&family=Open+Sans:wght@400;600&display=swap" rel="stylesheet">
<style>
  :root {
    --backdrop: #3a3a3c;
    --card: #ffffff;
    --ink: #1e1a1a;
    --muted: #444444;
    --gold-light: #efe6bd;
    --gold: #cdbb7a;
    --gold-deep: #a8934c;
  }
  html, body {
    margin: 0;
    width: 1200px;
    height: 852px;
    overflow: hidden;
    background: var(--backdrop);
    font-family: "Open Sans", Arial, sans-serif;
  }
  .stage {
    position: relative;
    width: 1200px;
    height: 852px;
  }
  .card {
    position: absolute;
    width: 525px;
    height: 300px;
    background: var(--card);
    border-radius: 22px;
    overflow: hidden;
    box-shadow: 0 10px 26px rgba(0,0,0,0.45);
  }
  .card--front { left: 50px; top: 276px; }
  .card--back  { left: 625px; top: 276px; }

  .card--front .edge {
    position: absolute;
    left: 0; right: 0; bottom: 0;
    height: 10px;
    background: linear-gradient(90deg, var(--gold-deep), var(--gold-light), var(--gold));
  }
  .wordmark {
    position: absolute;
    font-family: "Lobster", cursive;
    color: var(--ink);
    font-weight: 400;
    white-space: nowrap;
    line-height: 1;
  }
  .card--front .wordmark {
    left: 0; right: 0; top: 118px;
    text-align: center;
    font-size: 62px;
  }
  .card--back .wordmark {
    left: 30px; top: 96px;
    font-size: 44px;
  }
  .swoosh {
    position: absolute;
    inset: 0;
    width: 100%;
    height: 100%;
  }
  .holder {
    position: absolute;
    left: 56px; top: 176px;
  }
  .holder__name {
    font-family: "Lobster", cursive;
    font-size: 24px;
    color: var(--ink);
    line-height: 1;
  }
  .holder__role {
    font-size: 13px;
    color: var(--muted);
    margin-top: 4px;
    padding-left: 18px;
  }
  .contact {
    position: absolute;
    right: 16px; top: 66px;
    margin: 0; padding: 0;
    list-style: none;
    font-size: 11px;
    color: var(--ink);
    text-align: right;
    line-height: 17px;
  }
  .contact li { display: flex; justify-content: flex-end; align-items: center; gap: 5px; }
  .contact svg { width: 10px; height: 10px; flex: none; }
  .contact .spacer { width: 10px; }
  .address {
    position: absolute;
    right: 16px; top: 232px;
    font-size: 11px;
    color: var(--ink);
    white-space: nowrap;
  }
</style>
</head>
<body>
<main class="stage">
  <section class="card card--front" aria-label="Card front">
    <div class="wordmark">Shaker Barons</div>
    <div class="edge"></div>
  </section>

  <section class="card card--back" aria-label="Card back">
    <svg class="swoosh" viewBox="0 0 525 300" aria-hidden="true">
      <defs>
        <linearGradient id="goldFill" x1="0" y1="0" x2="1" y2="1">
          <stop offset="0" stop-color="#efe6bd"/>
          <stop offset="0.5" stop-color="#cdbb7a"/>
          <stop offset="1" stop-color="#a8934c"/>
        </linearGradient>
      </defs>
      <path d="M525 12 C420 14 360 42 338 110 C312 190 272 250 172 266 C100 277 50 279 0 281 L0 300 L525 300 Z" fill="url(#goldFill)"/>
      <path d="M525 6 C414 8 350 36 326 106 C300 184 262 242 162 258 C95 268 45 270 0 272" fill="none" stroke="#1e1a1a" stroke-width="5"/>
      <path d="M500 14 C420 26 370 60 346 120 C322 186 286 236 206 252 C140 264 70 262 0 258" fill="none" stroke="#1e1a1a" stroke-width="3"/>
      <path d="M0 291 C140 290 260 282 360 262" fill="none" stroke="#1e1a1a" stroke-width="4"/>
    </svg>

    <div class="wordmark">Shaker Barons</div>

    <div class="holder">
      <div class="holder__name">Rowan</div>
      <div class="holder__role">Cocktail Maker</div>
    </div>

    <ul class="contact">
      <li>0400118822
        <svg viewBox="0 0 10 10"><path d="M2 1 L4 1 L4.5 3 L3.5 4 C4 5.5 4.5 6 6 6.5 L7 5.5 L9 6 L9 8 C5 9 1 5 2 1 Z" fill="var(--ink)"/></svg>
      </li>
      <li>or 0400773311 <span class="spacer"></span></li>
      <li>/shakerbarons.net
        <svg viewBox="0 0 10 10"><rect x="1" y="1" width="8" height="8" rx="1.5" fill="var(--ink)"/></svg>
      </li>
      <li>info@shakerbarons.net
        <svg viewBox="0 0 10 10"><rect x="1" y="2" width="8" height="6" fill="var(--ink)"/><path d="M1 2 L5 5.5 L9 2" stroke="var(--gold-light)" stroke-width="0.8" fill="none"/></svg>
      </li>
      <li>www.shakerbarons.net
        <svg viewBox="0 0 10 10"><circle cx="5" cy="5" r="4" fill="none" stroke="var(--ink)" stroke-width="1.2"/><path d="M1 5 H9 M5 1 C3 3 3 7 5 9 C7 7 7 3 5 1" stroke="var(--ink)" stroke-width="0.8" fill="none"/></svg>
      </li>
      <li><span class="spacer"></span>
        <svg viewBox="0 0 10 10"><path d="M5 9.5 C2 6 2 4.5 2 4 A3 3 0 0 1 8 4 C8 4.5 8 6 5 9.5 Z" fill="var(--ink)"/><circle cx="5" cy="4" r="1.1" fill="var(--gold-light)"/></svg>
      </li>
    </ul>
    <div class="address">PO Box 4410 Palmview, Queensland, Australia</div>
  </section>
</main>
</body>
</html>
```